Business card for Tolvery Anesthesia LLC

This is for a business care for Tolvery Anesthesia LLC. Dr. Lisbeth Tolvery, CRNA, DNAP is the sole provider in the LLC. Business address is 4718 N Brackley Street,
Oakhaven, PA 17342
CRNA stands for certified registered nurse anesthetist
"Keeping you safe and comfortable"
I plan to give this business card to the patients that I provide anesthesia to.
Creative design that ties into Anesthesia. Calm soothing colors.

Target Market(s)

Business card for my patients.

Industry/Entity Type

Medicine

Contact Information for Business Card

Creative, professional, eye catching

Logo Text

Tolvery Anesthesia

Font styles to use
Serif
Script

Colors

Designer to choose colors to be used in the design.

Requirements
Must have
• Tolvery Anesthesia
• Dr. Lisbeth Tolvery, CRNA, DNAP
• tolvery.anesthesia@ quillmail.net
Nice to have
• "Keeping you safe and comfortable"
Should not have
• phone number

```html
<!DOCTYPE html>
<html lang="en">
<head>
<meta charset="utf-8">
<title>Tolvery Anesthesia LLC – Business Card</title>
<link rel="stylesheet" href="https://fonts.googleapis.com/css2?family=Crimson+Text:ital,wght@0,400;1,400&display=swap">
<style>
  :root {
    --backdrop: #2a2a2c;
    --sky: #4bb3e6;
    --deep-sky: #1676b9;
    --ocean: #1b7fb6;
    --sand: #e9a865;
    --stone: #8d8d8d;
    --paper: #ffffff;
    --mist: #eaf5fc;
  }
  * { margin: 0; padding: 0; box-sizing: border-box; }
  html, body {
    width: 1200px; height: 906px; overflow: hidden;
    background: var(--backdrop);
    font-family: "Crimson Text", "Times New Roman", serif;
  }
  .sheet {
    width: 1200px; height: 906px;
    display: flex; align-items: center; justify-content: center; gap: 30px;
  }
  .card {
    width: 560px; height: 320px; border-radius: 22px;
    position: relative; overflow: hidden; flex: none;
  }

  /* Shared lockup */
  .lockup { display: flex; align-items: center; gap: 18px; }
  .lockup__dot { border-radius: 50%; flex: none; }
  .lockup__text { display: flex; flex-direction: column; white-space: nowrap; }
  .brand-name {
    font-size: 28px; font-weight: 400; line-height: 1.1;
    padding-bottom: 5px;
  }
  .tagline {
    font-style: italic; font-size: 15px; padding-top: 4px; letter-spacing: .3px;
  }

  /* Front */
  .card--front {
    background: linear-gradient(160deg, var(--sky) 0%, var(--deep-sky) 100%);
    display: flex; align-items: center; justify-content: center;
  }
  .card--front .lockup__dot { width: 80px; height: 80px; border: 5px solid var(--mist); }
  .card--front .brand-name { color: var(--paper); border-bottom: 1px solid rgba(255,255,255,.55); }
  .card--front .tagline { color: var(--mist); }

  /* Back */
  .card--back { background: var(--paper); }
  .card--back .lockup { position: absolute; top: 38px; left: 120px; }
  .card--back .lockup__dot { width: 92px; height: 92px; border: 6px solid var(--ocean); }
  .card--back .brand-name { color: var(--ocean); border-bottom: 1px solid var(--stone); }
  .card--back .tagline { color: var(--stone); }

  .rule { position: absolute; left: 30px; right: 30px; height: 1px; background: var(--ocean); }
  .rule--top { top: 182px; }
  .rule--bottom { top: 262px; }

  .provider { position: absolute; left: 30px; top: 196px; white-space: nowrap; }
  .provider__name { color: var(--ocean); font-size: 23px; line-height: 1.2; }
  .provider__note { color: var(--sand); font-size: 14px; margin-top: 2px; }

  .contact {
    position: absolute; left: 30px; right: 30px; top: 274px;
    display: flex; align-items: center; gap: 7px;
    color: var(--ocean); font-size: 13px; white-space: nowrap;
  }
  .contact__icon { width: 14px; height: 14px; flex: none; }
  .contact__sep { color: var(--sand); margin: 0 3px; }
</style>
</head>
<body>
<main class="sheet">
  <section class="card card--front" aria-label="Card front">
    <div class="lockup">
      <span class="lockup__dot"></span>
      <div class="lockup__text">
        <span class="brand-name">Tolvery Anesthesia LLC</span>
        <span class="tagline">Keeping you safe and comfortable</span>
      </div>
    </div>
  </section>

  <section class="card card--back" aria-label="Card back">
    <div class="lockup">
      <span class="lockup__dot"></span>
      <div class="lockup__text">
        <span class="brand-name">Tolvery Anesthesia LLC</span>
        <span class="tagline">Keeping you safe and comfortable</span>
      </div>
    </div>

    <div class="rule rule--top"></div>

    <div class="provider">
      <p class="provider__name">Dr. Lisbeth Tolvery, CRNA, DNAP</p>
      <p class="provider__note">CRNA stands for certified registered nurse anesthetist</p>
    </div>

    <div class="rule rule--bottom"></div>

    <div class="contact">
      <svg class="contact__icon" viewBox="0 0 16 16" aria-hidden="true">
        <rect x="1" y="3" width="14" height="10" rx="1" fill="none" stroke="var(--sand)" stroke-width="1.6"/>
        <path d="M1.5 4 L8 9 L14.5 4" fill="none" stroke="var(--sand)" stroke-width="1.6"/>
      </svg>
      <span>tolvery.anesthesia@quillmail.net</span>
      <span class="contact__sep">|</span>
      <svg class="contact__icon" viewBox="0 0 16 16" aria-hidden="true">
        <path d="M8 1 C4.8 1 3 3.3 3 5.8 C3 9.3 8 15 8 15 C8 15 13 9.3 13 5.8 C13 3.3 11.2 1 8 1 Z" fill="var(--sand)"/>
        <circle cx="8" cy="5.9" r="2" fill="var(--paper)"/>
      </svg>
      <span>4718 N Brackley Street, Oakhaven, PA 17342</span>
    </div>
  </section>
</main>
</body>
</html>
```